Webshop / TarnvikLoom

professional webshop page with possibility to buy and email etc. the logo is already part of the website. at the bottom of the file I would like to create a complete home page with all the details

Industry/Entity Type

It Professional

Number of Pages Required

1 page

Colors

Designer to choose colors to be used in the design.

```html
<!DOCTYPE html>
<html lang="en">
<head>
<meta charset="utf-8">
<title>TarnvikLoom – Home</title>
<link href="https://fonts.googleapis.com/css2?family=Montserrat:wght@400;600;700&family=Open+Sans:wght@400;600;700&display=swap" rel="stylesheet">
<style>
:root{
  --green-dark:#0a5c1d;
  --green:#0b6a2a;
  --green-band:#06753f;
  --green-band-light:#0b8a4c;
  --gold:#8c7a10;
  --gold-line:#b49a1a;
  --grey-bg:#efefef;
  --card-bg:#ffffff;
  --blog-card:#ededed;
  --text:#4a4a4a;
  --text-dark:#222222;
  --footer:#4a4949;
  --footer-line:#5d5c5c;
  --white:#ffffff;
}
*{box-sizing:border-box;margin:0;padding:0}
html,body{width:1200px;height:3249px;overflow:hidden}
body{position:relative;font-family:"Open Sans",Arial,sans-serif;color:var(--text);background:var(--white)}
.abs{position:absolute}
h2.section-title{position:absolute;left:0;width:1200px;text-align:center;font-family:"Montserrat",Arial,sans-serif;font-weight:700;font-size:20px;color:var(--green);letter-spacing:.5px}
h2.section-title::after{content:"";display:block;width:52px;height:3px;background:var(--gold-line);margin:9px auto 0}

/* Header */
.site-header{position:absolute;top:0;left:0;width:1200px;height:134px;background:var(--green-dark)}
.brand{position:absolute;left:130px;top:40px;display:flex;align-items:center;gap:10px;font-family:"Montserrat",Arial,sans-serif;font-weight:700;font-size:26px;color:var(--white)}
.brand-dot{width:18px;height:18px;border-radius:50%;background:var(--gold-line)}
.call{position:absolute;left:878px;top:24px;display:flex;align-items:center;gap:14px;color:var(--white)}
.call-icon{width:42px;height:42px;border-radius:50%;background:#0f4d1a;display:flex;align-items:center;justify-content:center}
.call small{display:block;font-size:10px;font-weight:600}
.call strong{display:block;font-size:20px;font-weight:700;letter-spacing:.5px}
.main-nav{position:absolute;top:94px;left:520px;display:flex;gap:36px;font-family:"Montserrat",Arial,sans-serif;font-size:11px;font-weight:700;color:var(--white)}
.main-nav a{color:inherit;text-decoration:none;padding-bottom:9px}
.main-nav a.active{color:#d8c23a;border-bottom:2px solid #d8c23a}

/* Hero */
.hero{position:absolute;top:134px;left:0;width:1200px;height:511px;background:radial-gradient(ellipse at 28% 42%,#6fa33a 0%,#3d7421 30%,#1d3d12 65%,#0f1c0a 100%)}
.hero-copy{position:absolute;right:150px;top:135px;text-align:left;color:var(--white)}
.hero-copy .line1{font-size:40px;font-weight:700;letter-spacing:1px;line-height:1}
.hero-copy .line2{font-size:66px;font-weight:700;line-height:1.05;letter-spacing:1px}
.hero-copy .rule{height:2px;background:var(--white);margin:14px 0 10px;width:345px;opacity:.9}
.hero-copy .line3{font-size:25px;font-weight:400;letter-spacing:.5px}
.hero-copy .rule2{height:3px;background:#2a9a3a;width:345px;margin-top:8px}
.hero-dots{position:absolute;top:463px;left:560px;display:flex;gap:8px}
.hero-dots span{width:9px;height:9px;border-radius:50%;background:var(--white)}
.hero-dots span.on{background:#c8b02a}

/* Welcome */
.welcome-intro{position:absolute;top:760px;left:355px;width:490px;text-align:center;font-size:12px;line-height:1.6}
.feature{position:absolute;top:865px;width:200px;text-align:center}
.badge{width:110px;height:110px;margin:0 auto;display:block}
.feature h3{font-family:"Montserrat",Arial,sans-serif;font-weight:400;font-size:17px;color:var(--green);margin-top:24px}
.feature p{font-size:11px;line-height:1.4;margin-top:8px;padding:0 22px}

/* Product band */
.product-band{position:absolute;top:1133px;left:0;width:1200px;height:474px;background:var(--green-band);overflow:hidden}
.band-stripe{position:absolute;top:0;left:560px;width:900px;height:474px;background:var(--green-band-light);transform:skewX(-40deg);transform-origin:top left;opacity:.45}
.band-title{position:absolute;left:130px;top:34px;font-family:"Montserrat",Arial,sans-serif;font-weight:700;font-size:20px;color:var(--white)}
.band-title::after{content:"";display:block;width:50px;height:3px;background:var(--gold-line);margin-top:7px}
.band-lead{position:absolute;left:130px;top:86px;width:340px;font-size:13px;line-height:1.55;color:var(--white)}
.band-item{position:absolute;left:140px;display:flex;gap:22px;color:var(--white)}
.band-item svg{flex:none}
.band-item h4{font-family:"Montserrat",Arial,sans-serif;font-size:12px;font-weight:700}
.band-item p{font-size:10px;line-height:1.5;margin-top:5px;width:240px}
.btn{display:inline-block;background:var(--gold);color:var(--white);font-family:"Montserrat",Arial,sans-serif;font-weight:700;font-size:12px;text-decoration:none}
.band-btn{position:absolute;left:204px;top:398px;width:106px;height:35px;line-height:35px;text-align:center}
.tin-photo{position:absolute;left:510px;top:38px;width:560px;height:360px;border-radius:28px;background:linear-gradient(160deg,#e4e6e2 0%,#b8bcb6 45%,#1f6b34 46%,#135427 80%,#d9dbd6 81%)}

/* Our products */
.products{position:absolute;top:1607px;left:0;width:1200px;height:416px;background:var(--grey-bg)}
.product-card{position:absolute;top:152px;width:226px;height:216px;background:var(--card-bg);text-align:center}
.product-card .tab{position:absolute;left:88px;top:-24px;width:50px;height:50px;border-radius:50%;background:var(--card-bg);display:flex;align-items:center;justify-content:center}
.product-card h3{font-family:"Montserrat",Arial,sans-serif;font-weight:700;font-size:17px;color:var(--text-dark);margin-top:52px}
.product-card p{font-size:10.5px;line-height:1.45;margin:12px auto 0;width:170px}
.product-card a{display:block;margin-top:18px;font-family:"Montserrat",Arial,sans-serif;font-size:10.5px;font-weight:700;color:var(--gold);text-decoration:none}

/* Testimonials */
.testimonials{position:absolute;top:2023px;left:0;width:1200px;height:366px;background:radial-gradient(ellipse at 50% 40%,#1f7a37 0%,#125a24 55%,#0a3d16 100%)}
.testimonials h2{position:absolute;top:57px;width:1200px;text-align:center;font-family:"Montserrat",Arial,sans-serif;font-weight:700;font-size:20px;color:var(--white)}
.quote-text{position:absolute;top:140px;left:360px;width:500px;text-align:center;font-size:14px;line-height:1.55;color:var(--white)}
.quote-mark{position:absolute;font-family:Georgia,serif;font-size:72px;font-weight:700;color:var(--white);line-height:1}
.quote-name{position:absolute;top:279px;width:1200px;text-align:center;font-size:11px;font-weight:700;color:var(--white)}
.slide-arrow{position:absolute;top:178px}

/* Blog */
.blog-card{position:absolute;top:2523px;width:223px;background:var(--blog-card);padding:11px 11px 0}
.blog-card .thumb{width:201px;height:146px}
.blog-card h3{font-size:14px;font-weight:400;color:var(--text-dark);line-height:1.35;margin-top:18px}
.blog-card p{font-size:11px;line-height:1.5;margin-top:14px}
.blog-card .btn{font-size:9.5px;padding:5px 9px;margin:16px 0 24px}

/* Footer */
.site-footer{position:absolute;top:2976px;left:0;width:1200px;height:273px;background:var(--footer);color:var(--white)}
.footer-col{position:absolute;top:0;height:169px;text-align:center}
.footer-col h4{font-family:"Montserrat",Arial,sans-serif;font-size:12px;font-weight:700;margin-top:50px}
.footer-divider{position:absolute;top:0;width:4px;height:169px;background:var(--footer-line)}
.socials{display:flex;gap:7px;justify-content:center;margin-top:22px}
.socials span{width:24px;height:24px;border-radius:50%}
.footer-menu{font-size:11.5px;margin-top:22px;color:#dddddd}
.signup{display:flex;margin:25px auto 0;width:230px;height:34px}
.signup span{flex:1;background:#6b6a6a;font-size:11px;line-height:34px;text-align:left;padding-left:15px}
.signup b{width:66px;background:var(--gold);font-family:"Montserrat",Arial,sans-serif;font-size:10.5px;line-height:34px}
.footer-rule{position:absolute;top:169px;left:130px;width:940px;height:1px;background:#6a6969}
.copyright{position:absolute;top:211px;width:1200px;text-align:center;font-size:10.5px}
</style>
</head>
<body>

<header class="site-header">
  <div class="brand"><span class="brand-dot"></span>TarnvikLoom</div>
  <div class="call">
    <div class="call-icon">
      <svg width="20" height="20" viewBox="0 0 24 24"><path d="M6.6 10.8a15 15 0 0 0 6.6 6.6l2.2-2.2a1 1 0 0 1 1-.25 11.4 11.4 0 0 0 3.6.57 1 1 0 0 1 1 1V20a1 1 0 0 1-1 1A17 17 0 0 1 3 4a1 1 0 0 1 1-1h3.5a1 1 0 0 1 1 1c0 1.25.2 2.45.57 3.6a1 1 0 0 1-.25 1z" fill="#fff"/></svg>
    </div>
    <div><small>CALL US NOW</small><strong>555.010.2030</strong></div>
  </div>
  <nav class="main-nav">
    <a class="active" href="#">HOME</a><a href="#">ABOUT US</a><a href="#">SERVICES</a><a href="#">PRODUCTS</a><a href="#">BLOG</a><a href="#">TESTIMONIALS</a><a href="#">CONTACT US</a>
  </nav>
</header>

<section class="hero" role="img" aria-label="Close-up photo of a green hemp plant with serrated leaves on a dark background">
  <div class="hero-copy">
    <div class="line1">HOCHWERTIGER</div>
    <div class="line2">CBD-HANF</div>
    <div class="rule"></div>
    <div class="line3">100% SCHWEIZER PRODUKT</div>
    <div class="rule2"></div>
  </div>
  <div class="hero-dots"><span></span><span></span><span class="on"></span><span></span><span></span></div>
</section>

<h2 class="section-title" style="top:689px">WELCOME TO OUR SITE</h2>
<p class="welcome-intro">There are many variations of passages of Lorem Ipsum available, but the majority have suffered alteration in some form, by injected humour, or randomised words which look even slightly believable. If you are going to use a passage.</p>

<div class="feature" style="left:112px">
  <svg class="badge" viewBox="0 0 110 110"><circle cx="55" cy="55" r="52" fill="var(--green)"/><rect x="42" y="52" width="26" height="20" rx="2" fill="#fff"/><path d="M47 52v-7a8 8 0 0 1 16 0v7" stroke="#fff" stroke-width="4" fill="none"/></svg>
  <h3>Safe</h3><p>There are many variations of passages of Lorem Ipsum availa ble, but the majority.</p>
</div>
<div class="feature" style="left:355px">
  <svg class="badge" viewBox="0 0 110 110"><circle cx="55" cy="55" r="52" fill="var(--green)"/><rect x="38" y="52" width="8" height="20" fill="#fff"/><path d="M49 52l8-14c4 0 5 3 4 7l-1 5h10a3 3 0 0 1 3 4l-3 14a4 4 0 0 1-4 4H49z" fill="#fff"/></svg>
  <h3>Guaranteed</h3><p>There are many variations of passages of Lorem Ipsum availa ble, but the majority.</p>
</div>
<div class="feature" style="left:615px">
  <svg class="badge" viewBox="0 0 110 110"><circle cx="55" cy="55" r="52" fill="var(--green)"/><path d="M38 72c0-20 14-32 34-34 0 20-12 34-34 34z" fill="#fff"/><path d="M40 70l24-24" stroke="var(--green)" stroke-width="2.5"/></svg>
  <h3>100% Organic</h3><p>There are many variations of passages of Lorem Ipsum availa ble, but the majority.</p>
</div>
<div class="feature" style="left:886px">
  <svg class="badge" viewBox="0 0 110 110"><circle cx="55" cy="55" r="52" fill="var(--green)"/><path d="M38 62v-6a17 17 0 0 1 34 0v6" stroke="#fff" stroke-width="4" fill="none"/><rect x="35" y="58" width="9" height="15" rx="3" fill="#fff"/><rect x="66" y="58" width="9" height="15" rx="3" fill="#fff"/></svg>
  <h3>Support</h3><p>There are many variations of passages of Lorem Ipsum availa ble, but the majority.</p>
</div>

<section class="product-band">
  <div class="band-stripe"></div>
  <h2 class="band-title">OUR PRODUCT</h2>
  <p class="band-lead">There are many variations of passages of Lorem Ipsum available, but the majority have suffered .</p>
  <div class="band-item" style="top:160px">
    <svg width="42" height="38" viewBox="0 0 42 38"><circle cx="21" cy="19" r="14" fill="#fff"/></svg>
    <div><h4>ORGANIC HEMP</h4><p>There are many variations of passages of Lorem Ipsum availa ble, but the majority.</p></div>
  </div>
  <div class="band-item" style="top:240px">
    <svg width="42" height="38" viewBox="0 0 42 38"><path d="M21 6v26M13 32h16" stroke="#fff" stroke-width="3"/><circle cx="21" cy="12" r="6" fill="#fff"/></svg>
    <div><h4>THIRD PARTY TESTED</h4><p>There are many variations of passages of Lorem Ipsum availa ble, but the majority.</p></div>
  </div>
  <div class="band-item" style="top:320px">
    <svg width="42" height="38" viewBox="0 0 42 38"><path d="M11 18h20l-3 16H14z" fill="#fff"/><circle cx="21" cy="10" r="6" fill="#fff"/></svg>
    <div><h4>CANNABINOIDS</h4><p>There are many variations of passages of Lorem Ipsum availa ble, but the majority.</p></div>
  </div>
  <a class="btn band-btn" href="#">READ MORE</a>
  <div class="tin-photo" role="img" aria-label="Product photo of an open metal tin with a green label"></div>
</section>

<section class="products">
  <h2 class="section-title" style="top:46px">OUR PRODUCTS</h2>
  <div class="product-card" style="left:132px">
    <div class="tab"><svg width="22" height="30" viewBox="0 0 22 30"><rect x="8" y="1" width="6" height="6" fill="var(--gold)"/><rect x="4" y="8" width="14" height="21" rx="3" fill="var(--gold)"/></svg></div>
    <h3>CBD OIL</h3><p>There are many variations of passages of Lorem Ipsum available, but the majority have suffered alteration in some form, by injected humour.</p><a href="#">READ MORE ›</a>
  </div>
  <div class="product-card" style="left:368px">
    <div class="tab"><svg width="30" height="24" viewBox="0 0 30 24"><rect x="3" y="7" width="24" height="10" rx="5" fill="var(--gold)" transform="rotate(-25 15 12)"/></svg></div>
    <h3>CBD CAPSULES</h3><p>There are many variations of passages of Lorem Ipsum available, but the majority have suffered alteration in some form, by injected humour.</p><a href="#">READ MORE ›</a>
  </div>
  <div class="product-card" style="left:604px">
    <div class="tab"><svg width="16" height="32" viewBox="0 0 16 32"><rect x="5" y="0" width="6" height="6" fill="var(--gold)"/><rect x="2" y="7" width="12" height="24" rx="2" fill="var(--gold)"/></svg></div>
    <h3>CBD VAPE</h3><p>There are many variations of passages of Lorem Ipsum available, but the majority have suffered alteration in some form, by injected humour.</p><a href="#">READ MORE ›</a>
  </div>
  <div class="product-card" style="left:840px">
    <div class="tab"><svg width="30" height="28" viewBox="0 0 30 28"><ellipse cx="15" cy="19" rx="12" ry="8" fill="var(--gold)"/><circle cx="11" cy="7" r="4" fill="var(--gold)"/><circle cx="20" cy="5" r="3" fill="var(--gold)"/></svg></div>
    <h3>CBD SOAP</h3><p>There are many variations of passages of Lorem Ipsum available, but the majority have suffered alteration in some form, by injected humour.</p><a href="#">READ MORE ›</a>
  </div>
</section>

<section class="testimonials" role="img" aria-label="Soft-focus green hemp leaves as background">
  <h2>TESTIMONIALS</h2>
  <span class="quote-mark" style="left:320px;top:108px">“</span>
  <p class="quote-text">There are many variations of passages of Lorem Ipsum available, but the majority have suffered alteration in some form, by injected humour, or randomised words which don't look even slightly believable. If you are going to use a passage of Lorem Ipsum, you need to be sure there isn't anything embarrassing hidden in the middle of text.</p>
  <span class="quote-mark" style="left:740px;top:230px">”</span>
  <div class="quote-name">HALVARD</div>
  <svg class="slide-arrow" style="left:232px" width="22" height="36" viewBox="0 0 22 36"><path d="M18 4L5 18l13 14" stroke="#fff" stroke-width="4" fill="none"/></svg>
  <svg class="slide-arrow" style="left:922px" width="22" height="36" viewBox="0 0 22 36"><path d="M4 4l13 14L4 32" stroke="#fff" stroke-width="4" fill="none"/></svg>
</section>

<h2 class="section-title" style="top:2436px">LATEST BLOG</h2>
<article class="blog-card" style="left:132px">
  <div class="thumb" role="img" aria-label="Photo of dried hemp buds in a bowl" style="background:linear-gradient(135deg,#6f6a4a,#3c3a2a)"></div>
  <h3>Lorem Ipsum is simply dummy text of</h3>
  <p>There are many variations of passages of Lorem Ipsum available, but the majority have suffered alteration in some form, by injected humour, or randomised</p>
  <a class="btn" href="#">READ MORE</a>
</article>
<article class="blog-card" style="left:370px">
  <div class="thumb" role="img" aria-label="Photo of green hemp leaves" style="background:linear-gradient(135deg,#b9c9b0,#4f7a34)"></div>
  <h3>Lorem Ipsum is simply dummy text of</h3>
  <p>There are many variations of passages of Lorem Ipsum available, but the majority have suffered alteration</p>
  <a class="btn" href="#">READ MORE</a>
</article>
<article class="blog-card" style="left:609px">
  <div class="thumb" role="img" aria-label="Photo of a test tube with plant sample in a lab" style="background:linear-gradient(135deg,#dfe3df,#8a9a88)"></div>
  <h3>Lorem Ipsum is simply dummy text of</h3>
  <p>There are many variations of passages of Lorem</p>
  <a class="btn" href="#">READ MORE</a>
</article>
<article class="blog-card" style="left:845px">
  <div class="thumb" role="img" aria-label="Photo of golden oil poured onto a spoon" style="background:linear-gradient(135deg,#f2f2ee,#a9a33a)"></div>
  <h3>Lorem Ipsum is simply dummy text of</h3>
  <a class="btn" href="#">READ MORE</a>
</article>

<footer class="site-footer">
  <div class="footer-col" style="left:130px;width:238px">
    <h4>FOLLOW US</h4>
    <div class="socials"><span style="background:#3b5b9a"></span><span style="background:#1da1f2"></span><span style="background:#1d3f73"></span></div>
  </div>
  <div class="footer-divider" style="left:368px"></div>
  <div class="footer-col" style="left:372px;width:386px">
    <h4>MENU</h4>
    <div class="footer-menu">Home &nbsp;|&nbsp; About Us &nbsp;|&nbsp; Services &nbsp;|&nbsp; Products &nbsp;|&nbsp; Blog &nbsp;|&nbsp; Contact</div>
  </div>
  <div class="footer-divider" style="left:758px"></div>
  <div class="footer-col" style="left:762px;width:308px">
    <h4 style="margin-top:40px">NEWSLETTER SIGNUP</h4>
    <div class="signup"><span>E mail id</span><b>SIGNUP</b></div>
  </div>
  <div class="footer-rule"></div>
  <div class="copyright">Copyright © 2017 All Rights Reserved</div>
</footer>

</body>
</html>
```